trifold brochure Bright Harbour

We need a new tri fold brochure (A4 folded to DL) for our company Bright Harbour Paramedical Services Pty Ltd. We have just had a new logo created and this is attached.

The main products we are wanting to highlight are:
1. First Aid training
2. Automated External Defibrillators (mainly the Pulsar Quick Link and Pulsar Quickcase AEDs)
3. First Aid Kits and Supplies

Our website is www.brightharb.com.au This website will be redeveloped in the near future,based on the design of the brochure.

We have added a lot of photos here, please feel free to use what you wish and alter as necessary.

Target Market(s)

Businesses, corporations, and sporting groups. We specialise in corporate courses and do very little public first aid training

Industry/Entity Type

Training

Requirements
Must have
• We are different to our main competitors in that all trainers are Professional Paramedics. Files that can be read and altered in Illustrator CS2 or InDesign CS2.
Nice to have
• A tag line - open to suggestions. Information about Sudden Cardiac Arrest (included in word doc)

```html
<!DOCTYPE html>
<html lang="en">
<head>
<meta charset="utf-8">
<title>Bright Harbour Paramedical Services – Trifold Brochure</title>
<link href="https://fonts.googleapis.com/css2?family=Open+Sans:wght@400;600;700;800&display=swap" rel="stylesheet">
<style>
  :root {
    --stage: #e9e9e9;
    --red: #d8232a;
    --red-light: #ee4a50;
    --ink: #3a3a3a;
    --grey-panel: #e6e4e1;
    --grey-soft: #f1f0ee;
    --white: #ffffff;
    --swoosh-grey: #8f8f93;
  }
  * { box-sizing: border-box; margin: 0; padding: 0; }
  html, body { width: 1200px; height: 900px; overflow: hidden; }
  body {
    background: var(--stage);
    font-family: "Open Sans", Arial, sans-serif;
    color: var(--ink);
  }
  .brochure {
    position: absolute;
    left: 45px; top: 57px;
    width: 1110px; height: 786px;
    display: flex;
    box-shadow: 0 6px 24px rgba(0,0,0,.18);
    overflow: hidden;
  }
  .panel {
    position: relative;
    width: 370px; height: 100%;
    padding: 0 34px;
    z-index: 1;
  }
  .panel--about { background: linear-gradient(180deg, var(--grey-panel), var(--grey-soft) 70%); }
  .panel--courses { background: var(--white); }
  .panel--more { background: linear-gradient(180deg, var(--grey-panel), var(--grey-soft) 70%); }
  .panel + .panel { border-left: 1px solid rgba(0,0,0,.06); }

  .tab {
    margin: 0 -4px 30px;
    height: 56px;
    background: linear-gradient(180deg, var(--red-light), var(--red));
    border-radius: 0 0 28px 28px;
    display: flex; flex-direction: column; align-items: center; justify-content: center;
    overflow: hidden;
  }
  .tab__title {
    color: var(--white); font-weight: 700; font-size: 22px; letter-spacing: .5px; line-height: 1;
  }
  .tab__echo {
    color: var(--white); font-weight: 700; font-size: 22px; letter-spacing: .5px; line-height: 1;
    transform: scaleY(-1); opacity: .25; height: 10px; overflow: hidden;
  }

  p { font-size: 12.5px; line-height: 1.55; margin-bottom: 14px; }
  .course { margin-bottom: 16px; }
  .course__name {
    color: var(--red); font-weight: 700; font-size: 12.5px; line-height: 1.3; text-transform: uppercase;
    margin-bottom: 10px;
  }
  .course__name span { display: block; }
  .course p { text-indent: 14px; }

  .also__title { font-weight: 700; font-size: 13px; margin: 6px 0 6px 60px; }
  .also__list { list-style: none; font-size: 12.5px; line-height: 1.55; text-align: center; }
  .also__list li::before { content: "• "; }

  .includes { list-style: none; font-size: 12px; line-height: 1.6; margin: 4px 0 12px 30px; }
  .includes li::before { content: "• "; }
  .includes--wide { margin-left: 50px; }
  .note { font-weight: 700; font-size: 13px; margin: 6px 0 8px 40px; }

  .swoosh {
    position: absolute; left: 0; top: 0; width: 1110px; height: 786px; z-index: 0;
  }
  .device-photo {
    position: absolute; left: 36px; bottom: 54px;
    width: 250px; height: 170px; z-index: 2;
    border-radius: 10px;
    background: linear-gradient(160deg, #dfe5ee 0%, #b9c3d3 55%, #4f86c6 100%);
  }
</style>
</head>
<body>
<div class="brochure">
  <svg class="swoosh" viewBox="0 0 1110 786" aria-hidden="true">
    <path d="M0 640 C260 600 520 700 1110 520 L1110 786 L0 786 Z" fill="#f3f3f3"/>
    <path d="M0 700 C200 650 330 690 470 660 C700 610 900 560 1110 430 L1110 470 C900 610 700 670 470 720 C320 750 180 740 0 760 Z" fill="#d8232a"/>
    <path d="M0 740 C240 700 500 760 1110 600 L1110 786 L0 786 Z" fill="#b81a20"/>
    <path d="M0 600 C300 560 560 660 1110 470" fill="none" stroke="#8f8f93" stroke-width="10" opacity=".7"/>
    <path d="M0 620 C320 590 600 640 1110 500" fill="none" stroke="#b0b0b4" stroke-width="4"/>
    <path d="M380 560 C560 600 760 560 1110 360" fill="none" stroke="#d8232a" stroke-width="2"/>
    <path d="M400 590 C600 620 820 560 1110 390" fill="none" stroke="#d8232a" stroke-width="1.5"/>
    <path d="M420 520 C640 600 840 640 1110 620" fill="none" stroke="#8f8f93" stroke-width="3"/>
    <path d="M600 500 C760 560 900 620 1110 560" fill="none" stroke="#8f8f93" stroke-width="6" opacity=".6"/>
    <path d="M0 660 C220 620 420 700 740 640" fill="none" stroke="#ffffff" stroke-width="2" opacity=".8"/>
  </svg>

  <section class="panel panel--about">
    <div class="tab"><span class="tab__title">ABOUT US</span><span class="tab__echo">ABOUT US</span></div>
    <p>Bright Harbour Paramedical Services Pty Ltd offers quality first aid training to schools, businesses, and organisations.</p>
    <p>We offer a range of First Aid Courses that are recognised throughout Australia. The certificate each participant receives is also recognised Australia wide.</p>
    <p>By providing accredited trainers who are also professional paramedics, we ensure our courses are of the highest standard. Our trainers live what they teach everyday. They have performed CPR on the lounge room floor, managed victims of heart attack, and school children suffering asthma attacks.</p>
    <h3 class="also__title">We also:</h3>
    <ul class="also__list">
      <li>develop tailored courses for business</li>
      <li>conduct training at your premises</li>
      <li>offer ongoing support to participants</li>
      <li>send out reaccreditation reminders</li>
      <li>monthly e-mail of First Aid updates</li>
    </ul>
    <div class="device-photo" role="img" aria-label="Photo of a Pulsar Quick Link defibrillator in its blue carry case"></div>
  </section>

  <section class="panel panel--courses">
    <div class="tab"><span class="tab__title">COURSES</span><span class="tab__echo">COURSES</span></div>
    <div class="course">
      <h3 class="course__name"><span>Perform CPR</span><span>(HLTCPR201A)</span></h3>
      <p>Participants gain the skills and knowledge required to perform Cardiopulmonary Resuscitation (CPR) in line with the National Resuscitation Board guidelines.</p>
    </div>
    <div class="course">
      <h3 class="course__name"><span>Basic Life Support</span><span>(HLTFA201A)</span></h3>
      <p>Frequently known as Level 1 First Aid. Participants are introduced to the skills and background knowledge required to recognise / respond to life threatening emergencies using basic life support techniques until a more qualified medically trained person is available.</p>
    </div>
    <div class="course">
      <h3 class="course__name"><span>Apply First Aid</span><span>(HLTFA301B)</span></h3>
      <p>Also frequently known as level 2 First Aid. This course represents the level of First Aid certification required by most industries and employers. Participants develop First Aid skills that may be applied in a range of situations, including community and workplace settings.</p>
      <p>This course can be delivered by flexible learning, reducing the time your employees are out of the office.</p>
    </div>
  </section>

  <section class="panel panel--more">
    <div class="tab"><span class="tab__title">COURSES</span><span class="tab__echo">COURSES</span></div>
    <div class="course">
      <h3 class="course__name"><span>Automated External Defibrillation</span><span>(21658VIC)</span></h3>
      <p>Participants develop the necessary skills to safely and effectively resuscitate a patient in cardiac arrest using a Automated External Defibrillator and Cardiopulmonary Resuscitation in line with the National Resuscitation Board guidelines.</p>
    </div>
    <div class="course">
      <h3 class="course__name"><span>First Aid Management of Anaphylaxis</span><span>(21659VIC)</span></h3>
      <p>Participants develop the skills and knowledge to provide first aid to a patient suffering from anaphylaxis.</p>
      <p style="margin:0 0 2px 14px">Course includes:</p>
      <ul class="includes">
        <li>Anaphylaxis Risk Minimisation</li>
        <li>Anaphylaxis Management Plans</li>
        <li>Recognition &amp; Treatment of Anaphylaxis</li>
        <li>Use of AdreJect or AllerPen</li>
      </ul>
    </div>
    <div class="course">
      <h3 class="course__name"><span>First Aid for Parents</span></h3>
      <p>A brief course encompassing all the “must know” elements of first aid for the parents of infants and toddlers.</p>
      <h4 class="note">Includes:</h4>
      <ul class="includes includes--wide">
        <li>CPR for babies &amp; children</li>
        <li>Choking</li>
        <li>Short of Breath (Asthma, Croup)</li>
      </ul>
      <p style="margin-left:40px;text-indent:0">Designed to fit into the busy schedule of new mums &amp; dads, whilst not breaking their budget.</p>
    </div>
  </section>
</div>
</body>
</html>
```